We Need a GREAT Looking Sales Flyer!

Our small, boutique fitness facility needs a new flyer which highlights a new entry level fitness program that we are launching.

The flyer should be visually appealing as we will be handing a full color version to the potential member during our sales process.

I have attached:
- a word document which includes text
-Photos that can be used. Not all need to be used. These are to be used as you feel appropriate
- Our Logo

```html
<!DOCTYPE html>
<html lang="en">
<head>
<meta charset="UTF-8">
<title>Kickstart Program Flyer</title>
<link href="https://fonts.googleapis.com/css2?family=Anton&family=Montserrat:wght@400;600;800&family=Open+Sans:wght@400;800&display=swap" rel="stylesheet">
<style>
  :root {
    --backdrop: #c77aaa;
    --hero-pink: #f46ed6;
    --band-magenta: #cf5bb2;
    --deep-plum: #8a3d78;
    --lime: #a8e021;
    --ink: #1c1c1c;
    --white: #ffffff;
    --brand-blue: #1f7fd6;
  }
  * { box-sizing: border-box; margin: 0; padding: 0; }
  html, body {
    width: 1200px; height: 840px; overflow: hidden;
    background: var(--backdrop);
  }
  .flyer {
    position: absolute; left: 270px; top: 15px;
    width: 660px; height: 810px;
    background: var(--band-magenta);
    overflow: hidden;
    box-shadow: 0 18px 40px rgba(90, 20, 70, 0.35);
  }
  .hero-panel {
    position: absolute; left: 0; top: 0; width: 295px; height: 345px;
    background: var(--hero-pink);
    padding: 48px 30px 0 42px;
  }
  .hero-title {
    font-family: "Open Sans", sans-serif; font-weight: 800;
    font-size: 31px; line-height: 1.15; color: var(--ink);
  }
  .hero-sub {
    margin-top: 16px;
    font-family: "Open Sans", sans-serif; font-weight: 400;
    font-size: 15px; line-height: 1.35; color: var(--ink);
  }
  .brand {
    position: absolute; left: 42px; top: 262px;
    display: flex; align-items: center; gap: 10px;
    font-family: "Open Sans", sans-serif; font-weight: 800;
    font-size: 24px; letter-spacing: 1px; color: var(--brand-blue);
  }
  .brand-dot { width: 14px; height: 14px; background: var(--brand-blue); }
  .hero-photo {
    position: absolute; left: 295px; top: 0; width: 365px; height: 345px;
    background: linear-gradient(160deg, #6f7da0 0%, #d9cfe0 35%, #3b4256 70%, #22262f 100%);
  }
  .col {
    position: absolute; top: 378px;
    color: var(--white);
    font-family: "Montserrat", sans-serif; font-weight: 400;
    font-size: 11px; line-height: 1.45;
  }
  .col-kickstart { left: 40px; width: 270px; }
  .col-benefits { left: 360px; width: 230px; top: 400px; }
  .col-heading {
    font-family: "Anton", sans-serif; font-weight: 400;
    font-size: 34px; line-height: 1.02; margin-bottom: 12px;
  }
  .col-heading .accent, .accent { color: var(--lime); }
  .col-heading.is-lime { color: var(--lime); }
  .chevrons { position: absolute; }
  .chevrons-back { left: 560px; top: 378px; }
  .chevrons-forward { left: 190px; top: 612px; }
  .tagline {
    position: absolute; left: 130px; top: 570px;
    font-family: "Montserrat", sans-serif; font-weight: 800;
    font-size: 16px; letter-spacing: 2px; color: var(--white);
  }
  .offer {
    position: absolute; left: 385px; top: 640px; width: 260px;
    font-family: "Montserrat", sans-serif; font-weight: 800;
    font-size: 21px; line-height: 1.25; color: var(--lime);
  }
  .art-corner {
    position: absolute; left: 0; top: 660px; width: 320px; height: 150px;
    background: var(--deep-plum);
  }
  .art-illustration {
    position: absolute; left: 60px; top: 672px; width: 230px; height: 138px;
    background: linear-gradient(180deg, #f3dde6 0%, #e9c4c9 100%);
  }
</style>
</head>
<body>
  <main class="flyer">
    <section class="hero-panel">
      <h1 class="hero-title">Change Begins<br>NOW!</h1>
      <p class="hero-sub">The Fitness Program that is responsible for transforming over 924+ lives!</p>
    </section>
    <div class="brand"><span class="brand-dot"></span>Elmridge Studio</div>
    <div class="hero-photo" role="img" aria-label="Photo of a woman doing dumbbell lunges in a busy group training gym"></div>

    <section class="col col-kickstart">
      <h2 class="col-heading">The Ultimate<br><span class="accent">Kickstart</span></h2>
      <p>(2) Detailed Body Scans to track results<br>
      Supplement List to accelerate metabolism<br>
      10% off First Supplement Purchase to Kickstart the process<br>
      Exclusive access to FitVela's Private Community Page for additional recipes, Support and Guidance</p>
    </section>

    <section class="col col-benefits">
      <h2 class="col-heading is-lime">What you get</h2>
      <p>Unlimited Group Training Designed Specifically to Sculpt &amp; Tone the body<br>
      CUSTOM Meal Plan designed specifically for Your and Your Body Type</p>
    </section>

    <svg class="chevrons chevrons-back" width="80" height="60" viewBox="0 0 80 60">
      <polyline points="38,6 12,30 38,54" fill="none" stroke="#a8e021" stroke-width="10"/>
      <polyline points="72,6 46,30 72,54" fill="none" stroke="#a8e021" stroke-width="10"/>
    </svg>

    <p class="tagline">The Life That You Envision IS <span class="accent">POSSIBLE!</span></p>

    <svg class="chevrons chevrons-forward" width="120" height="60" viewBox="0 0 120 60">
      <polyline points="8,6 34,30 8,54" fill="none" stroke="#a8e021" stroke-width="10"/>
      <polyline points="44,6 70,30 44,54" fill="none" stroke="#a8e021" stroke-width="10"/>
      <polyline points="80,6 106,30 80,54" fill="none" stroke="#a8e021" stroke-width="10"/>
    </svg>

    <p class="offer">Get started for<br>$199 (crossed out) ONLY<br>$99limited time</p>

    <div class="art-corner"></div>
    <div class="art-illustration" role="img" aria-label="Illustration of a woman meditating cross-legged on a mat"></div>
  </main>
</body>
</html>
```